依頼詳細
起業をしようと思っているが
具体的にはどのようにしていいのかわからない方向けに
比較的安価でセミナーを開催しようと考えています。

希望しては、信頼感とフレンドリーさを感じられるサイトデザインを
提案していただければ幸いです。

参考として他社で気に入っているサイトは下記になります。
http://www.mirevo-kaigi.example/kanyu/yutai.html?ref=QZ7pLm4TxR2vNk8WdYs3HaBfE

また文章部分については自分でも考えますので
「******」などの伏せ字にしていただいても結構です。

たたき台として案をエクセルファイルにまとめまてあります。
必ずしもエクセルにある文章通りにしたりする必要はなく
構成を変えていただいたり、キャッチコピーを変えるなど
むしろしていただければ幸いです。
文章や構成などをうまく編集していただいた方には
万が一、当選しなくても、別に参加賞などで対応させていただきます。

今回はデザインのみでコーディングは不要です。
皆様、
非常に素晴らしい力作をご提案いただきありがとうございます。

まだ
提案予約をしていただいていますが
提出ができていない方がいらっしゃるため
期限を少し伸ばしたいと思います。

引き続きすばらしい作品をお待ちしております。
こちらのサイトの姉妹サイトで
簡単なTOPページの画像修正を
新規のTOBIRASの案件として依頼中です。

もしご興味のある人がいましたらば
ぜひご参加のほどよろしくお願い致します。

http://www.tobiras-works.example/job/view/527394
皆様、ご応募ありがとうございます。
これから選考に入らせていただきます。

このあと修正の可否などお伺いすることもあるかと思いますが
可能であればご返信いただければ幸いです。

1週間程度で最終的な採択をさせていただくつもりです。
それではよろしくお願い致します。

デザイン性が高く
ファーストビューで当事務所がお客様に伝えたいことを
的確に表現していただいた点

提案してくださいましたランサーの皆様
多くの素晴らしいデザインを提案していただいてありがとうございました。
また今後もデザインを発注することがあると思いますので
その際はどうぞよろしくお願い致します。

```html
<!DOCTYPE html>
<html lang="ja">
<head>
<meta charset="utf-8">
<title>起業・独立セミナー | 森川浩一公認会計士事務所</title>
<link href="https://fonts.googleapis.com/css2?family=Noto+Sans+JP:wght@400;500;700;900&family=Noto+Serif+JP:wght@500;700&display=swap" rel="stylesheet">
<style>
:root{
  --ink:#222;
  --muted:#555;
  --navy:#1b3f73;
  --orange:#f5a21a;
  --orange-dark:#e07f00;
  --green:#7cbf2a;
  --green-dark:#5c9b16;
  --red:#c8161d;
  --red-dark:#9a0e12;
  --cream:#fff8e6;
  --line:#d9d9d9;
  --bg:#ffffff;
  --band:#f3f3f3;
  --dark:#2a2a2a;
}
*{box-sizing:border-box;margin:0;padding:0}
html,body{width:1200px;height:4652px;overflow:hidden;background:var(--bg);color:var(--ink);font-family:"Noto Sans JP",sans-serif}
.page{width:1200px;height:4652px;position:relative}
.wrap{width:1080px;margin:0 auto;position:relative}

/* header */
.site-header{height:80px;border-bottom:1px solid var(--line)}
.site-header .wrap{display:flex;align-items:center;height:80px}
.brand{font-family:"Noto Serif JP",serif;font-size:22px;font-weight:700;color:var(--ink);flex:1}
.tel{display:flex;align-items:center;gap:10px;font-size:34px;font-weight:700;color:var(--red);margin-right:28px}
.btn-small{border:1px solid #bbb;border-radius:4px;padding:8px 16px;font-size:16px;background:linear-gradient(#fff,#eee);display:flex;gap:8px;align-items:center}

/* hero */
.hero{height:440px;background:linear-gradient(#fff,#f4f4f4);position:relative;overflow:hidden}
.hero .wrap{height:440px}
.hero-title{font-size:64px;font-weight:900;color:var(--navy);padding-top:28px;letter-spacing:2px}
.hero-sub{font-size:34px;font-weight:700;color:var(--navy);margin:6px 0 0 70px}
.worries{position:absolute;left:0;top:200px;width:560px;background:#fff;border:2px solid var(--orange);border-radius:6px;padding:18px 24px;box-shadow:0 2px 6px rgba(0,0,0,.15)}
.worries h2{font-size:26px;font-weight:700;margin-bottom:10px}
.worries li{list-style:none;display:flex;align-items:center;gap:12px;font-size:19px;font-weight:700;background:#fdf3dc;margin-top:8px;padding:7px 10px}
.hero-photo{position:absolute;right:40px;top:0;width:380px;height:440px;background:linear-gradient(#f2f2f2,#d8d8d8)}
.solve-band{height:80px;background:linear-gradient(#3a6fb0,#1b3f73);color:#fff;text-align:center;font-size:40px;font-weight:900;line-height:80px;letter-spacing:3px;position:relative}
.solve-arrow{display:block;margin:0 auto}

/* cta */
.cta{margin:60px auto 0;width:1080px;height:150px;background:var(--cream);border:2px solid #f3d48a;display:flex;align-items:center;padding:0 40px;gap:40px}
.cta p{font-size:22px;font-weight:700;color:var(--orange-dark);line-height:1.6;flex:1}
.btn-apply{width:440px;height:80px;border-radius:8px;background:linear-gradient(#ffc04a,var(--orange-dark));color:#fff;font-size:32px;font-weight:700;display:flex;align-items:center;justify-content:center;box-shadow:0 3px 0 #b86300}

/* features */
.features{width:1080px;margin:50px auto 0;display:grid;grid-template-columns:1fr 1fr;gap:40px 40px}
.feature{position:relative;height:280px}
.badge{position:absolute;left:0;top:0;width:110px;height:110px;border-radius:50%;background:var(--orange);color:#fff;text-align:center;font-weight:700;font-size:16px;padding-top:14px;z-index:2;box-shadow:0 2px 4px rgba(0,0,0,.2)}
.badge b{display:block;font-size:48px;line-height:1}
.feature h3{margin-left:90px;margin-top:20px;height:50px;background:linear-gradient(var(--green),var(--green-dark));color:#fff;font-size:22px;font-weight:700;line-height:50px;padding-left:40px}
.feature ul{margin:20px 0 0 130px;list-style:none}
.feature li{font-size:17px;color:var(--muted);line-height:1.95}
.feature li::before{content:"・"}

/* instructor */
.profile{width:1080px;margin:40px auto 0;height:340px;position:relative}
.profile-head{display:flex;align-items:center;gap:40px;border-bottom:2px solid var(--dark);width:620px}
.profile-head span{background:var(--dark);color:#fff;font-size:28px;font-weight:700;padding:8px 40px}
.profile-head strong{font-size:30px}
.profile p{font-size:20px;line-height:1.8;margin-top:24px;font-weight:500}
.profile p + p{margin-top:18px}
.profile-photo{position:absolute;right:40px;top:0;width:340px;height:320px;background:linear-gradient(#e8ecef,#b7c0c7)}

/* voices */
.section-title{font-size:34px;font-weight:700;color:var(--navy);border-bottom:3px solid var(--navy);padding-bottom:6px}
.voices{width:1080px;margin:60px auto 0}
.voice{display:flex;gap:40px;margin-top:40px;height:280px;background:linear-gradient(#fff,#f4f4f4);border-bottom:1px solid var(--line);padding-bottom:20px}
.voice-photo{width:300px;height:240px;background:#111;flex:none}
.voice h3{font-size:28px;font-weight:700;border-bottom:1px solid var(--line);padding-bottom:8px}
.voice .who{font-size:20px;font-weight:700;margin:14px 0 10px}
.voice .who span{margin-left:36px}
.voice .comment{font-size:16px;color:var(--muted);line-height:1.8;word-break:break-all}

/* qa */
.qa{width:1080px;margin:60px auto 0}
.qa .section-title{color:var(--orange-dark);border-color:var(--orange)}
.qa-item{margin-top:40px;border:1px solid var(--line);background:#fafafa}
.qa-q{font-size:28px;font-weight:700;padding:16px 24px;border-bottom:1px solid var(--line);background:#fff}
.qa-a{display:flex;gap:20px;padding:18px 24px}
.qa-a b{font-size:30px}
.qa-a p{font-size:16px;color:var(--muted);line-height:1.9}

/* form */
.entry{width:1080px;margin:120px auto 0}
.entry-head{height:64px;background:linear-gradient(#3a3a3a,#111);color:#fff;font-size:32px;font-weight:700;display:flex;align-items:center;gap:20px;position:relative}
.entry-head::before{content:"";width:80px;height:80px;border-radius:50%;background:var(--red);margin-left:-10px}
.form-table{width:100%;border-collapse:collapse;margin-top:20px;font-size:16px}
.form-table th{width:280px;background:#eee;text-align:left;padding:14px 24px;border:1px solid var(--line);font-weight:500}
.form-table td{padding:12px 24px;border:1px solid var(--line)}
.field{height:34px;border:1px solid #bbb;width:460px;background:#fff}
.field.area{height:120px;width:600px}
.dates label{display:block;line-height:1.9}
.dates .full{color:#999;text-decoration:line-through}
.dates .full em{color:var(--red);font-style:normal;text-decoration:none;margin-left:12px}
.btn-submit{width:400px;height:80px;margin:40px auto 0;border-radius:8px;background:linear-gradient(#e8333a,var(--red-dark));color:#fff;font-size:32px;font-weight:700;display:flex;align-items:center;justify-content:center;box-shadow:0 3px 0 #6d0a0d}

.site-footer{position:absolute;left:0;bottom:0;width:1200px;height:52px;background:var(--dark);color:#aaa;font-size:13px;text-align:center;line-height:52px}
</style>
</head>
<body>
<div class="page">

<header class="site-header">
  <div class="wrap">
    <div class="brand">森川浩一公認会計士事務所</div>
    <div class="tel">
      <svg width="30" height="30" viewBox="0 0 24 24"><path fill="#c8161d" d="M6.6 10.8a15 15 0 0 0 6.6 6.6l2.2-2.2c.3-.3.7-.4 1-.2 1.1.4 2.3.6 3.6.6.6 0 1 .4 1 1V20c0 .6-.4 1-1 1A17 17 0 0 1 3 4c0-.6.4-1 1-1h3.5c.6 0 1 .4 1 1 0 1.3.2 2.5.6 3.6.1.3 0 .7-.2 1z"/></svg>
      03-5550-0142
    </div>
    <div class="btn-small">
      <svg width="12" height="12" viewBox="0 0 12 12"><path d="M3 1l6 5-6 5z" fill="#e07f00"/></svg>
      お申し込みはこちらから
    </div>
  </div>
</header>

<section class="hero">
  <div class="wrap">
    <h1 class="hero-title">起業・独立セミナー</h1>
    <p class="hero-sub">～起業を志す方の学びの場、交流の場</p>
    <div class="worries">
      <h2>こんな悩みありませんか？</h2>
      <ul>
        <li><svg width="22" height="22" viewBox="0 0 22 22"><rect x="1" y="1" width="20" height="20" fill="#c8161d"/><path d="M5 11l4 4 8-9" stroke="#fff" stroke-width="3" fill="none"/></svg>起業をしたいがまず何をはじめたらいいかわからない</li>
        <li><svg width="22" height="22" viewBox="0 0 22 22"><rect x="1" y="1" width="20" height="20" fill="#c8161d"/><path d="M5 11l4 4 8-9" stroke="#fff" stroke-width="3" fill="none"/></svg>税金？銀行から融資？起業について不安がある</li>
        <li><svg width="22" height="22" viewBox="0 0 22 22"><rect x="1" y="1" width="20" height="20" fill="#c8161d"/><path d="M5 11l4 4 8-9" stroke="#fff" stroke-width="3" fill="none"/></svg>起業について相談する仲間がほしい</li>
      </ul>
    </div>
  </div>
  <div class="hero-photo" role="img" aria-label="スーツ姿の女性講師の写真"></div>
</section>

<div class="solve-band">このセミナーで悩みを解決しませんか？</div>
<svg class="solve-arrow" width="120" height="30" viewBox="0 0 120 30"><path d="M0 0h120L60 30z" fill="#1b3f73"/></svg>

<section class="cta">
  <p>セミナーは毎月第1、3土曜日10時からです。<br>リーズナブルな料金でしっかり学習できる！<br>定員がございます。今すぐお申込みはこちら！</p>
  <div class="btn-apply">お申込みはこちらから</div>
</section>

<section class="features">
  <article class="feature">
    <div class="badge">解決その<b>1</b></div>
    <h3>基礎からわかる丁寧な講義</h3>
    <ul><li>最初の基礎から講義します</li><li>さらに応用まで身につく内容です</li><li>知らないと損をする税金について</li></ul>
  </article>
  <article class="feature">
    <div class="badge">解決その<b>2</b></div>
    <h3>本当の起業ノウハウ</h3>
    <ul><li>専門家による実務の講義内容</li><li>10年以上の支援実績に基づく解説</li><li>メガバンク出身者による融資の話</li><li>創業計画書の書き方を学ぶ</li><li>100社以上の起業支援経験</li><li>資料を持ち帰って復習できる</li></ul>
  </article>
  <article class="feature">
    <div class="badge">解決その<b>3</b></div>
    <h3>わからないところはいつでも質問できる体制</h3>
    <ul><li>少人数制</li><li>10名までの少人数なので気軽に質問可</li><li>質問できるのもポイント</li></ul>
  </article>
  <article class="feature">
    <div class="badge">解決その<b>4</b></div>
    <h3>起業の仲間ができる</h3>
    <ul><li>最大のメリットはここ</li><li>起業を志す仲間と出会える場です</li><li>同じ時期に起業を目指している</li><li>同じ悩みを持つ方と話せる</li><li>そして励まし合える関係に</li><li>さらに交流会も開催します</li></ul>
  </article>
</section>

<section class="profile">
  <div class="profile-head"><span>講師略歴</span><strong>森川 浩一</strong></div>
  <p>東都大学大学院経営学研究科（MBA）卒業<br>公認会計士・税理士<br>監査法人、外資系コンサルティング会社<br>ひかり中央銀行を経て独立</p>
  <p>起業に特化したコンサルティングおよび会計事務所を運営<br>上場企業、大学、VCなどでのセミナー経験も豊富</p>
  <div class="profile-photo" role="img" aria-label="講師のスーツ姿の写真"></div>
</section>

<section class="voices">
  <h2 class="section-title">参加者の声</h2>
  <article class="voice">
    <div class="voice-photo" role="img" aria-label="参加者の写真"></div>
    <div>
      <h3>この起業セミナーに参加して</h3>
      <p class="who">株式会社＊＊＊<span>青木さん</span></p>
      <p class="comment">コメントコメントコメントコメントコメントコメントコメントコメントコメントコメントコメントコメントコメントコメントコメントコメントコメントコメントコメントコメントコメントコメントコメントコメントコメントコメント</p>
    </div>
  </article>
  <article class="voice">
    <div class="voice-photo" role="img" aria-label="参加者の写真"></div>
    <div>
      <h3>この起業セミナーに参加して</h3>
      <p class="who">株式会社＊＊＊<span>青木さん</span></p>
      <p class="comment">コメントコメントコメントコメントコメントコメントコメントコメントコメントコメントコメントコメントコメントコメントコメントコメントコメントコメントコメントコメントコメントコメントコメント</p>
    </div>
  </article>
  <article class="voice">
    <div class="voice-photo" role="img" aria-label="参加者の写真"></div>
    <div>
      <h3>この起業セミナーに参加して</h3>
      <p class="who">株式会社＊＊＊<span>青木さん</span></p>
      <p class="comment">コメントコメントコメントコメントコメントコメントコメントコメントコメントコメントコメントコメントコメントコメントコメントコメントコメントコメントコメントコメントコメントコメントコメントコメントコメント</p>
    </div>
  </article>
</section>

<section class="qa">
  <h2 class="section-title">よくあるQ＆A</h2>
  <div class="qa-item">
    <div class="qa-q">Q、質問が入ります。</div>
    <div class="qa-a"><b>A、</b><p>答えが入ります。答えが入ります。答えが入ります。答えが入ります。答えが入ります。答えが入ります。答えが入ります。答えが入ります。答えが入ります。答えが入ります。答えが入ります。答えが入ります。答えが入ります。答えが入ります。答えが入ります。答えが入ります。答えが入ります。答えが入ります。答えが入ります。答えが入ります。答えが入ります。答えが入ります。答えが入ります。</p></div>
  </div>
  <div class="qa-item">
    <div class="qa-q">Q、質問が入ります。</div>
    <div class="qa-a"><b>A、</b><p>答えが入ります。答えが入ります。答えが入ります。答えが入ります。答えが入ります。答えが入ります。答えが入ります。答えが入ります。答えが入ります。答えが入ります。答えが入ります。答えが入ります。答えが入ります。答えが入ります。答えが入ります。答えが入ります。答えが入ります。答えが入ります。答えが入ります。答えが入ります。答えが入ります。答えが入ります。答えが入ります。</p></div>
  </div>
</section>

<section class="entry">
  <h2 class="entry-head">申し込みフォーム</h2>
  <table class="form-table">
    <tr><th>参加希望日</th><td class="dates">
      <label class="full">○ 4/18(土) 10時〜 東京都立会議室<em>満席になりました</em></label>
      <label>○ 5/9(土) 10時〜 東京都立会議室</label>
      <label>○ 5/16(土) 10時〜 東京都立会議室</label>
    </td></tr>
    <tr><th>お名前</th><td><div class="field"></div></td></tr>
    <tr><th>メールアドレス</th><td><div class="field"></div></td></tr>
    <tr><th>お電話番号</th><td><div class="field"></div></td></tr>
    <tr><th>備考</th><td><div class="field area"></div></td></tr>
  </table>
  <div class="btn-submit">お申込みはこちらから</div>
</section>

<footer class="site-footer">Copyright © 森川浩一公認会計士事務所 All Rights Reserved.</footer>
</div>
</body>
</html>
```